Green Energy Conservation Business Cards

We believe in Conserve before you produce energy. I am looking for a unique, bold business card. that Demonstrates Expertise in our field. I would be interested to try and incorporate a night picture of the US or world showing the yellow lights on one side. I would be open to a design that caters to half the business card size height and same length. Our primary expertise is Energy projects for self storage. Use either black or white background .Attached are the logos and symbols.

May I see some design utilizing a smaller business card. the same length as a normal business card but cut in half on the height. best regards Garvel

```html
<!DOCTYPE html>
<html lang="en">
<head>
<meta charset="utf-8">
<title>Velta Energy Group – Slim Business Cards</title>
<link rel="stylesheet" href="https://fonts.googleapis.com/css2?family=Arimo:wght@400;700&display=swap">
<style>
  :root {
    --stage: #1c1c1e;
    --card: #0b0b0c;
    --card-edge: #1f1f22;
    --brand-blue: #1f7fd4;
    --brand-green: #8cd23a;
    --green-light: #a6e24a;
    --green-deep: #5db62c;
    --text-light: #f2f2f2;
    --text-muted: #cfcfcf;
  }
  * { box-sizing: border-box; margin: 0; padding: 0; }
  html, body {
    width: 1200px;
    height: 900px;
    overflow: hidden;
    background: var(--stage);
    font-family: "Arimo", Arial, sans-serif;
  }
  .canvas {
    position: relative;
    width: 1200px;
    height: 900px;
  }
  .card {
    position: absolute;
    left: 250px;
    width: 700px;
    height: 200px;
    background: linear-gradient(135deg, #121214 0%, var(--card) 60%, #050506 100%);
    border: 1px solid var(--card-edge);
    overflow: hidden;
    box-shadow: 0 18px 40px rgba(0,0,0,0.55);
  }
  .card--front { top: 180px; }
  .card--back  { top: 500px; }

  /* front */
  .accent-band {
    position: absolute;
    left: 0; top: 0;
    width: 250px; height: 100%;
    background: linear-gradient(160deg, var(--green-light) 0%, var(--brand-green) 50%, var(--green-deep) 100%);
  }
  .front-identity {
    position: absolute;
    right: 44px;
    top: 40px;
    text-align: right;
  }
  .company-name {
    color: var(--brand-blue);
    font-weight: 700;
    font-size: 38px;
    letter-spacing: 0.3px;
    line-height: 1.1;
    white-space: nowrap;
  }
  .website {
    margin-top: 30px;
    color: var(--text-light);
    font-size: 19px;
    letter-spacing: 0.3px;
  }

  /* back */
  .back-identity {
    position: absolute;
    left: 34px;
    top: 0;
    height: 100%;
    display: flex;
    align-items: center;
    gap: 12px;
  }
  .brand-dot {
    width: 30px; height: 30px;
    border-radius: 50%;
    background: var(--brand-green);
    flex: none;
  }
  .back-identity .company-name { font-size: 26px; }
  .contact {
    position: absolute;
    left: 400px;
    top: 26px;
    color: var(--text-light);
    font-size: 14px;
    line-height: 1.35;
    white-space: nowrap;
  }
  .person-name {
    font-size: 19px;
    font-weight: 400;
    margin-bottom: 1px;
  }
  .person-name .first { color: var(--brand-blue); }
  .person-name .last { color: var(--brand-green); }
  .person-title { color: var(--text-muted); font-size: 13px; margin-bottom: 14px; }
  .label-phone { color: var(--brand-blue); }
  .label-email { color: var(--brand-green); }
  .address { margin-top: 12px; }
</style>
</head>
<body>
<main class="canvas">
  <section class="card card--front" aria-label="Card front">
    <div class="accent-band"></div>
    <div class="front-identity">
      <div class="company-name">Velta Energy Group</div>
      <div class="website">www.VeltaEnergy.com</div>
    </div>
  </section>

  <section class="card card--back" aria-label="Card back">
    <div class="back-identity">
      <span class="brand-dot"></span>
      <span class="company-name">Velta Energy Group</span>
    </div>
    <div class="contact">
      <div class="person-name"><span class="first">Mason</span> <span class="last">Garvel</span></div>
      <div class="person-title">President</div>
      <div><span class="label-phone">P:</span> (209) 555-0142</div>
      <div><span class="label-email">E:</span> mason@veltaenergy.com</div>
      <div class="address">27 W Birch Ln<br>Riverton CA 95370</div>
    </div>
  </section>
</main>
</body>
</html>
```